Need Business Cards for my Business

email address: rkpmarlowhollowworks@vendrimail.com
web address: rkpmarlowhollowworks.net
Slogan: We offer various QVN licenses
Rowland K. Pemberly
Please stick with colors of Company Logo
would like the card to be more of the color example of the logo.
If you need PDF copy of logo email me at the above account.
Creative control rests with you.

Industry/Entity Type

Business

Contact Information for Business Card

I am a minimalist, but would like something to pop and stand out amongst other cards, make it memorable.

Font styles to use
Serif
Decorative
Script

```html
<!DOCTYPE html>
<html lang="en">
<head>
<meta charset="utf-8">
<title>Marlow Hollow Works – Business Cards</title>
<link rel="stylesheet" href="https://fonts.googleapis.com/css2?family=Open+Sans:wght@400;600&display=swap">
<style>
  :root {
    --page-bg: #e9e6e1;
    --card-white: #ffffff;
    --card-grey: #eef0f2;
    --blue-deep: #1a5ea6;
    --blue-mid: #1d7fc4;
    --blue-light: #2a9fd8;
    --accent-red: #e5323f;
    --name-blue: #2a8fd0;
    --text-white: #ffffff;
    --brand-navy: #1f3f7a;
  }
  html, body {
    margin: 0;
    padding: 0;
    width: 1200px;
    height: 1023px;
    overflow: hidden;
    background: var(--page-bg);
    font-family: "Open Sans", Arial, sans-serif;
  }
  .canvas {
    position: relative;
    width: 1200px;
    height: 1023px;
  }
  .card {
    position: absolute;
    width: 620px;
    height: 354px;
    border-radius: 14px;
    overflow: hidden;
    box-shadow: 0 10px 24px rgba(0,0,0,0.18);
  }
  /* Front */
  .card-front {
    left: 80px;
    top: 100px;
    background: linear-gradient(180deg, var(--card-white), var(--card-grey));
  }
  .card-front .wave {
    position: absolute;
    inset: 0;
    width: 100%;
    height: 100%;
  }
  .brand-mark {
    position: absolute;
    left: 40px;
    top: 150px;
    display: flex;
    align-items: center;
    gap: 10px;
  }
  .brand-mark .dot {
    width: 14px;
    height: 14px;
    border-radius: 50%;
    background: var(--brand-navy);
  }
  .brand-mark .brand-name {
    font-size: 20px;
    font-weight: 600;
    color: var(--brand-navy);
    white-space: nowrap;
  }
  .holder-name {
    position: absolute;
    left: 40px;
    top: 268px;
    margin: 0;
    font-size: 20px;
    font-weight: 400;
    color: var(--name-blue);
    white-space: nowrap;
  }
  .contact-list {
    position: absolute;
    right: 24px;
    top: 48px;
    margin: 0;
    padding: 0;
    list-style: none;
    color: var(--text-white);
    font-size: 11px;
    line-height: 24px;
    white-space: nowrap;
  }
  .contact-list li {
    display: flex;
    justify-content: flex-end;
    align-items: center;
    gap: 8px;
  }
  .contact-list svg {
    width: 12px;
    height: 12px;
    flex: none;
  }
  /* Back */
  .card-back {
    left: 500px;
    top: 560px;
    background: radial-gradient(ellipse at 60% 40%, var(--blue-light), var(--blue-mid) 45%, var(--blue-deep));
    color: var(--text-white);
  }
  .back-brand {
    position: absolute;
    left: 0;
    right: 0;
    top: 122px;
    margin: 0;
    text-align: center;
    font-size: 34px;
    font-weight: 600;
    letter-spacing: 2px;
    text-transform: uppercase;
    white-space: nowrap;
  }
  .slogan {
    position: absolute;
    left: 0;
    right: 0;
    top: 188px;
    margin: 0;
    display: flex;
    justify-content: center;
    align-items: center;
    gap: 14px;
    font-size: 14px;
    letter-spacing: 1.5px;
    white-space: nowrap;
  }
  .slogan .rule {
    width: 34px;
    height: 1px;
    background: var(--text-white);
  }
</style>
</head>
<body>
<main class="canvas">

  <section class="card card-front" aria-label="Business card front">
    <svg class="wave" viewBox="0 0 620 354" preserveAspectRatio="none" aria-hidden="true">
      <defs>
        <linearGradient id="waveBlue" x1="0" y1="0" x2="0" y2="1">
          <stop offset="0" stop-color="#239bd6"/>
          <stop offset="1" stop-color="#1a5ea6"/>
        </linearGradient>
      </defs>
      <path d="M310 0 C 290 80, 300 160, 298 240 C 296 300, 285 330, 282 354 L 304 354 C 307 330, 318 300, 320 240 C 322 160, 312 80, 332 0 Z" fill="var(--accent-red)"/>
      <path d="M352 0 C 332 80, 342 160, 340 240 C 338 300, 327 330, 324 354 L 620 354 L 620 0 Z" fill="url(#waveBlue)"/>
    </svg>

    <div class="brand-mark">
      <span class="dot"></span>
      <span class="brand-name">Marlow Hollow Works</span>
    </div>

    <h1 class="holder-name">Rowland K. Pemberly</h1>

    <ul class="contact-list">
      <li>55-987-60412
        <svg viewBox="0 0 16 16"><circle cx="8" cy="8" r="7" fill="none" stroke="#fff" stroke-width="1.3"/><path d="M5.5 4.5l1.5 1.5-1 1.2c.6 1.2 1.5 2.1 2.7 2.7l1.2-1 1.5 1.5-1 1.1c-2.6-.3-5.2-2.9-5.5-5.5z" fill="#fff"/></svg>
      </li>
      <li>rkpmarlowhollowworks@vendrimail.com
        <svg viewBox="0 0 16 16"><rect x="1" y="3" width="14" height="10" fill="#fff"/><path d="M1 3l7 6 7-6" fill="none" stroke="#1d7fc4" stroke-width="1.2"/></svg>
      </li>
      <li>www.rkpmarlowhollowworks.net
        <svg viewBox="0 0 16 16"><g fill="none" stroke="#fff" stroke-width="1.2"><circle cx="8" cy="8" r="7"/><ellipse cx="8" cy="8" rx="3" ry="7"/><path d="M1 8h14M2.5 4.5h11M2.5 11.5h11"/></g></svg>
      </li>
    </ul>
  </section>

  <section class="card card-back" aria-label="Business card back">
    <h2 class="back-brand">Marlow Hollow Works</h2>
    <p class="slogan"><span class="rule"></span>We offer various QVN licenses<span class="rule"></span></p>
  </section>

</main>
</body>
</html>
```